Tolvane Global Wordpress website design

We need a worddpress website/theme design for a new outsourcing company based in Australia.Name of the company is "Tolvane".
Website content is in progress.
The design needs to be clean without clutter in any section. Some example websites are provided below
Menu
- Resources
- Services
- Our difference
Home page needs to have a gif image, for example http://www.brindleworks.example. or http://www.corvathicket.example or http://www.corvathicket.example/team.html
We like how the corvathicket website flows without having the need to click on the menu. It is also mobile friendly (which is important)
Each piece of content will have a learn more button
A call to action button will be placed on the home page, which will provide our phone number and access to online form*
A call to action button will also be added to various other pages such as Resources.
Resources Section will contain web articles, whitepapers, blog and any other ccontent which helps customer in making a decision
Having the ability to add a video or images on the home page is also important
Ability to edit the content easily via wordpress is extremely important
* This is a great Contact Us form - http://www.pelgrastudio.example/#/schedule-meeting
* We do not need the traditional web form on the contact us page
Target Market(s)
Small to medium businesses requiring outsourcing services
Industry/Entity Type
It Company
Coding
Coded - Design and coding required
Colors
Designer to choose colors to be used in the design.
Look and feel
Each slider illustrates characteristics of the customer's brand and the style your logo design should communicate.

```html
<!DOCTYPE html>
<html lang="en">
<head>
<meta charset="utf-8">
<title>Tolvane — Website/theme design</title>
<link rel="stylesheet" href="https://fonts.googleapis.com/css2?family=Poppins:wght@400;500;600;700&display=swap">
<style>
  :root {
    --ink: #3a3a3c;
    --text: #4a4a4a;
    --muted: #5c5c5c;
    --accent: #e5232f;
    --paper: #ffffff;
    --photo-office: #5b6a80;
    --photo-office-2: #2d3f66;
    --photo-warm: #8c7058;
    --photo-warm-2: #c9b59a;
  }
  * { box-sizing: border-box; margin: 0; padding: 0; }
  html, body { width: 1200px; height: 2866px; overflow: hidden; background: var(--paper); }
  body { position: relative; font-family: "Poppins", sans-serif; color: var(--text); }

  .site-header .brand {
    position: absolute; left: 76px; top: 34px;
    display: flex; align-items: center; gap: 10px;
    font-size: 15px; font-weight: 600; color: var(--ink);
  }
  .brand-mark { width: 12px; height: 12px; background: var(--accent); }
  .back-link {
    position: absolute; left: 186px; top: 34px;
    font-size: 14px; font-weight: 600; color: var(--accent); text-decoration: none;
  }
  .menu-toggle { position: absolute; left: 1098px; top: 34px; }

  .page-title {
    position: absolute; left: 229px; top: 156px; width: 780px;
    font-size: 53px; line-height: 48px; font-weight: 700; color: var(--ink);
    letter-spacing: 0.2px;
  }
  .body-copy {
    position: absolute; left: 281px; width: 640px;
    font-size: 12px; line-height: 20px; color: var(--text);
  }
  .body-copy .hl { color: var(--accent); }
  .lead-copy {
    position: absolute; left: 281px; width: 645px;
    font-size: 15.5px; line-height: 23px; font-weight: 600; color: var(--ink);
  }
  .lead-copy .hl { color: var(--accent); }

  .media {
    position: absolute; left: 281px; width: 636px;
  }
  .media-video { top: 447px; height: 321px; background: linear-gradient(120deg, var(--photo-office) 0%, #3b4a63 55%, var(--photo-office-2) 100%); }
  .media-mission { top: 1095px; height: 323px; background: linear-gradient(110deg, var(--photo-warm) 0%, #6e5a4c 50%, var(--photo-warm-2) 100%); }
  .play-button { position: absolute; left: 560px; top: 568px; }

  .btn {
    position: absolute; left: 281px; width: 178px; height: 38px;
    display: flex; align-items: center; justify-content: space-between;
    padding: 0 16px 0 22px;
    font-size: 10.5px; letter-spacing: 1.2px; text-transform: uppercase; text-decoration: none;
  }
  .btn-primary { top: 917px; background: var(--accent); color: #fff; }
  .btn-outline { top: 2746px; border: 1.5px solid var(--accent); color: var(--ink); }

  .section-title {
    position: absolute; left: 229px;
    font-size: 25px; font-weight: 500; color: var(--accent);
  }

  .team-member { position: absolute; width: 193px; }
  .team-photo { height: 208px; background: linear-gradient(160deg, #b9b4ad, #6f6962); }
  .team-member:nth-child(2n) .team-photo { background: linear-gradient(160deg, #a7b3bd, #55606a); }
  .team-member:nth-child(3n) .team-photo { background: linear-gradient(160deg, #9a8f88, #3d3735); }
  .team-name {
    margin-top: 22px; font-size: 20px; line-height: 23px; font-weight: 600;
    color: var(--ink); letter-spacing: 0.6px;
  }
  .team-role { margin-top: 12px; font-size: 11px; color: var(--muted); }
</style>
</head>
<body>
  <header class="site-header">
    <div class="brand"><span class="brand-mark"></span>Tolvane</div>
    <a class="back-link" href="#">— Back</a>
    <svg class="menu-toggle" width="26" height="20" viewBox="0 0 26 20" aria-label="Menu">
      <rect x="0" y="1" width="26" height="2" fill="#555"/>
      <rect x="0" y="9" width="26" height="2" fill="#555"/>
      <rect x="0" y="17" width="26" height="2" fill="#555"/>
    </svg>
  </header>

  <main>
    <h1 class="page-title">Website/theme design for a new outsourcing company based in Australia</h1>

    <p class="body-copy" style="top:330px">Lorem Ipsum is simply dummy text of the printing and typesetting industry. Lorem Ipsum has been the industry's standard dummy text ever since the 1500s, when an unknown printer took a galley of type and scrambled it to make a type specimen book. It has survived not only five centuries, but also the leap into electronic typesetting, remaining essentially unchanged.</p>

    <div class="media media-video" role="img" aria-label="Video still: team members working at desks in a bright office"></div>
    <svg class="play-button" width="80" height="80" viewBox="0 0 80 80" aria-label="Play video">
      <circle cx="40" cy="40" r="38" fill="none" stroke="#fff" stroke-width="2.5"/>
      <path d="M33 26 L56 40 L33 54 Z" fill="#fff"/>
    </svg>

    <p class="body-copy" style="top:802px">Lorem Ipsum is simply dummy text of the printing and typesetting industry. Lorem Ipsum has been the industry's standard dummy text ever since the 1500s, when an unknown printer took a galley of type and scrambled it to make a type specimen book. It has survived not only five centuries, but also the leap into electronic typesetting, remaining essentially unchanged.</p>

    <a class="btn btn-primary" href="#">Explore more
      <svg width="14" height="16" viewBox="0 0 14 16"><path d="M2 1 L12 8 L2 15 L5 8 Z" fill="none" stroke="#fff" stroke-width="1.6" stroke-linejoin="round"/></svg>
    </a>

    <h2 class="section-title" style="top:1030px">Our Mission</h2>
    <div class="media media-mission" role="img" aria-label="Photo: two colleagues smiling while reviewing a tablet in a sunlit café"></div>

    <p class="body-copy" style="top:1450px">Lorem Ipsum is simply dummy text of the printing and typesetting industry. Lorem Ipsum has been the industry's standard dummy text ever since the 1500s, when an unknown printer took a galley of type and scrambled it to make a type specimen book.</p>

    <p class="lead-copy" style="top:1526px">Lorem Ipsum is simply dummy text of the printing and typesetting industry. Lorem Ipsum has been the industry's standard dummy text ever since the 1500s, <span class="hl">when an unknown printer took a galley</span> of type and scrambled it to make a type specimen book.</p>

    <p class="body-copy" style="top:1634px">Lorem Ipsum is simply dummy text of the printing and typesetting industry. Lorem Ipsum has been the industry's standard dummy text ever since the 1500s, <span class="hl">when an unknown printer took a galley</span> of type and scrambled it to make a type specimen book.</p>

    <h2 class="section-title" style="top:1764px">Tolvane Team</h2>

    <p class="body-copy" style="top:1820px">Tolvane &nbsp;runs a unique recruitment campaign – resulting in a team of 200 extraordinary players and bright minds from almost 40 different nations, all of whom celebrate and contribute to our company culture, and collectively work towards a mutual goal and purpose.</p>
    <p class="body-copy" style="top:1902px">Meet some of us below.</p>

    <section class="team">
      <div class="team-member" style="left:281px;top:1955px">
        <div class="team-photo" role="img" aria-label="Portrait of the founder and CEO"></div>
        <h3 class="team-name">Aldric<br>Venholm</h3>
        <p class="team-role">Founder and CEO</p>
      </div>
      <div class="team-member" style="left:503px;top:1955px">
        <div class="team-photo" role="img" aria-label="Portrait of the co-founder"></div>
        <h3 class="team-name">Tobin<br>Marchetti</h3>
        <p class="team-role">Co-Founder</p>
      </div>
      <div class="team-member" style="left:724px;top:1955px">
        <div class="team-photo" role="img" aria-label="Portrait of the creative director"></div>
        <h3 class="team-name">Sorcha<br>Velland-Okoro</h3>
        <p class="team-role">Creative Director</p>
      </div>
      <div class="team-member" style="left:281px;top:2293px">
        <div class="team-photo" role="img" aria-label="Portrait of the head of technology"></div>
        <h3 class="team-name">Idris<br>Calloway</h3>
        <p class="team-role">Head of Technology</p>
      </div>
      <div class="team-member" style="left:503px;top:2293px">
        <div class="team-photo" role="img" aria-label="Portrait of the people and culture lead"></div>
        <h3 class="team-name">Mirelle<br>Tanaway</h3>
        <p class="team-role">People and Culture</p>
      </div>
      <div class="team-member" style="left:724px;top:2293px">
        <div class="team-photo" role="img" aria-label="Portrait of the legal counsel"></div>
        <h3 class="team-name">Rowan<br>Pelling</h3>
        <p class="team-role">Legal Counsel</p>
      </div>
    </section>

    <p class="lead-copy" style="top:2664px;font-size:14.5px;line-height:22px">We pride in being an award-winning <span class="hl">support team</span> in Customer Satisfaction Lorem Ipsum is simply dummy text</p>

    <a class="btn btn-outline" href="#">Contact us
      <svg width="14" height="16" viewBox="0 0 14 16"><path d="M2 1 L12 8 L2 15 L5 8 Z" fill="none" stroke="#e5232f" stroke-width="1.6" stroke-linejoin="round"/></svg>
    </a>
  </main>
</body>
</html>
```